Boutique Store Selling Antiques and Unique Finds

I need a Web Page designed for my Store Called "Harrow Lane". I would like a very classic, muted design that looks European when pulled up. I will be selling Antiques from all over the world and Unique finds that have reproduced. I will also be selling high-end purses and jewelry with unique, reasonable products for the every-day buyer as well.

Target Market(s)

25-70 year old men and women;)

Coding

Number of Pages Required

1 page

Colors

Designer to choose only greyscale colors for use in the design.

Requirements
Must have
• I want it

```html
<!DOCTYPE html>
<html lang="en">
<head>
<meta charset="utf-8">
<title>Harrow Lane — Antiques &amp; Unique Finds</title>
<link href="https://fonts.googleapis.com/css2?family=EB+Garamond:wght@400;500;700&family=Roboto:wght@400&display=swap" rel="stylesheet">
<style>
  :root {
    --ink: #1b1b1a;
    --paper: #f5f5f4;
    --paper-alt: #efefee;
    --white: #ffffff;
    --gold: #b88a2c;
    --gold-bright: #dca833;
    --grey-arrow: #8a8a8a;
    --grey-text: #d2d2d2;
    --date-box: #353534;
    --nav-muted: #8c8c8c;
  }
  * { margin: 0; padding: 0; box-sizing: border-box; }
  html, body { width: 780px; height: 1200px; overflow: hidden; }
  body {
    position: relative;
    background: var(--paper);
    font-family: "EB Garamond", Georgia, serif;
    color: var(--ink);
  }
  .abs { position: absolute; }

  /* Hero */
  .hero { left: 0; top: 0; width: 780px; height: 374px; background: var(--paper); }
  .hero-shape { left: 0; top: 0; }
  .hero-photo {
    left: 318px; top: 108px; width: 350px; height: 230px;
    border-radius: 45% 45% 40% 40% / 35% 35% 55% 55%;
    background: radial-gradient(ellipse at 50% 45%, #e3b64c 0%, #c38f2a 45%, #7a5614 80%, rgba(40,30,10,0) 100%);
  }
  .header {
    left: 112px; top: 15px; width: 556px; height: 53px;
    background: var(--white);
    box-shadow: 0 1px 3px rgba(0,0,0,0.08);
  }
  .brand {
    left: 10px; top: 13px;
    display: flex; flex-direction: column; align-items: center;
    font-size: 15px; font-weight: 500; letter-spacing: 3px; text-transform: uppercase;
    color: var(--ink);
  }
  .brand-dot { width: 10px; height: 10px; border-radius: 50%; background: var(--ink); margin-bottom: 3px; }
  .utility {
    right: 9px; top: 14px;
    font-family: "Roboto", Arial, sans-serif; font-size: 6.5px; color: var(--nav-muted);
    letter-spacing: 0.2px;
  }
  .utility span.sep { margin: 0 4px; }
  .nav { right: 9px; top: 33px; display: flex; gap: 17px; font-size: 7.5px; text-transform: uppercase; }
  .nav a { color: var(--ink); text-decoration: none; padding-bottom: 3px; }
  .nav a.active { color: var(--gold); border-bottom: 1px solid var(--gold); }

  .hero-title { left: 112px; top: 145px; font-size: 31px; font-weight: 700; line-height: 1; }
  .hero-sub { left: 112px; top: 188px; font-size: 27px; line-height: 1; }
  .btn-outline {
    left: 112px; top: 235px; width: 133px; height: 34px;
    border: 1px solid var(--ink); background: transparent;
    font-size: 12.5px; text-transform: uppercase; letter-spacing: 0.3px;
    display: flex; align-items: center; justify-content: center;
  }
  .arrow { width: 16px; height: 12px; }

  /* Shop */
  .shop { left: 0; top: 374px; width: 780px; height: 375px; background: var(--paper-alt); }
  .shop-title {
    left: 0; top: 51px; width: 780px; text-align: center;
    font-size: 33px; color: var(--gold); line-height: 1;
  }
  .card { top: 97px; width: 176px; height: 211px; background: var(--white); }
  .card-photo { width: 176px; height: 182px; }
  .card-caption { height: 29px; display: flex; align-items: center; justify-content: center; font-size: 11.5px; }

  /* Events + newsletter */
  .events { left: 0; top: 749px; width: 780px; height: 382px; background: #f7f7f6; }
  .events-title { left: 112px; top: 31px; font-size: 32px; color: var(--white); line-height: 1; }
  .event-date {
    left: 112px; top: 83px; width: 119px; height: 35px;
    background: var(--date-box); color: var(--gold-bright);
    font-size: 17px; display: flex; align-items: center; justify-content: center;
  }
  .event-text {
    left: 112px; top: 131px; width: 260px;
    font-family: "Roboto", Arial, sans-serif; font-size: 12.3px; line-height: 24.5px; color: var(--grey-text);
  }
  .view-all {
    left: 113px; top: 219px;
    font-family: "Roboto", Arial, sans-serif; font-size: 11.5px; color: var(--grey-text);
    text-decoration: underline; text-underline-offset: 2px;
  }
  .signup-title {
    right: 112px; top: 185px; text-align: right;
    font-size: 32px; line-height: 37px; text-transform: uppercase;
  }
  .email-field {
    left: 457px; top: 267px; width: 211px; height: 34px;
    border: 1px solid var(--ink); background: var(--white);
    font-size: 12px; color: #8a8a8a; padding-left: 14px; display: flex; align-items: center;
  }
  .btn-subscribe {
    left: 457px; top: 310px; width: 211px; height: 34px;
    background: var(--gold-bright); color: var(--ink);
    font-size: 14px; display: flex; align-items: center; justify-content: center;
  }

  /* Footer */
  .footer { left: 0; top: 1131px; width: 780px; height: 69px; background: var(--paper-alt); }
  .copyright {
    left: 112px; top: 30px;
    font-family: "Roboto", Arial, sans-serif; font-size: 9px; color: var(--ink);
  }
  .social { top: 26px; width: 20px; height: 20px; border-radius: 50%; background: #454545; }
</style>
</head>
<body>

<section class="hero abs">
  <svg class="hero-shape abs" width="780" height="374" aria-hidden="true">
    <polygon points="515,0 780,0 780,374 249,374" fill="var(--ink)"/>
  </svg>
  <div class="hero-photo abs" role="img" aria-label="Gilded antique crown set with clear stones"></div>

  <header class="header abs">
    <div class="brand abs"><span class="brand-dot"></span>Harrow Lane</div>
    <div class="utility abs">SEARCH<span class="sep">|</span>MY ACCOUNT<span class="sep">|</span>BASKET (0)</div>
    <nav class="nav abs">
      <a class="active" href="#">Antiques</a>
      <a href="#">Unique Finds</a>
      <a href="#">Shop Online</a>
      <a href="#">Discover</a>
      <a href="#">News</a>
      <a href="#">Contact</a>
    </nav>
  </header>

  <h1 class="hero-title abs">Lorem ipsum</h1>
  <p class="hero-sub abs">dolor consectetur</p>
  <div class="btn-outline abs">Find out more</div>

  <svg class="arrow abs" style="left:20px;top:215px" viewBox="0 0 16 12" aria-hidden="true"><path d="M15 6H2M7 1L2 6l5 5" stroke="var(--grey-arrow)" stroke-width="2" fill="none"/></svg>
  <svg class="arrow abs" style="left:745px;top:215px" viewBox="0 0 16 12" aria-hidden="true"><path d="M1 6h13M9 1l5 5-5 5" stroke="var(--grey-arrow)" stroke-width="2" fill="none"/></svg>
</section>

<section class="shop abs">
  <h2 class="shop-title abs">OUR SHOP</h2>
  <svg class="arrow abs" style="left:20px;top:182px" viewBox="0 0 16 12" aria-hidden="true"><path d="M15 6H2M7 1L2 6l5 5" stroke="var(--grey-arrow)" stroke-width="2" fill="none"/></svg>
  <svg class="arrow abs" style="left:745px;top:182px" viewBox="0 0 16 12" aria-hidden="true"><path d="M1 6h13M9 1l5 5-5 5" stroke="var(--grey-arrow)" stroke-width="2" fill="none"/></svg>

  <article class="card abs" style="left:112px">
    <div class="card-photo" role="img" aria-label="Jewelled antique brass crown on a stand" style="background:linear-gradient(180deg,#e4d8c6 0%,#9c7f4c 55%,#3a3835 100%)"></div>
    <div class="card-caption">Lorem ipsum</div>
  </article>
  <article class="card abs" style="left:302px">
    <div class="card-photo" role="img" aria-label="Carved stone statue of a crowned king beside a wooden staircase" style="background:linear-gradient(90deg,#6e3b1c 0%,#b9ad97 45%,#c8bfae 60%,#7a4220 100%)"></div>
    <div class="card-caption">Lorem ipsum</div>
  </article>
  <article class="card abs" style="left:492px">
    <div class="card-photo" role="img" aria-label="Antique silver campaign medal on a blue ribbon" style="background:linear-gradient(180deg,#d8cdbd 0%,#9aa6ad 30%,#8a8276 65%,#d6cab8 100%)"></div>
    <div class="card-caption">Lorem ipsum</div>
  </article>
</section>

<section class="events abs">
  <svg class="abs" style="left:0;top:0" width="780" height="382" aria-hidden="true">
    <polygon points="0,0 539,0 257,382 0,382" fill="var(--ink)"/>
  </svg>
  <h2 class="events-title abs">WHAT’S ON</h2>
  <div class="event-date abs">Feb 10, 2021</div>
  <p class="event-text abs">Fusce sollicitudin lorem et luctus volutpat. Proin placerat dapibus gravida. In tristique tristique nulla eget hendrerit.</p>
  <a class="view-all abs">VIEW ALL</a>

  <h2 class="signup-title abs">Sign up for<br>newsletter</h2>
  <div class="email-field abs">Email ID</div>
  <div class="btn-subscribe abs">SUBSCRIBE</div>
</section>

<footer class="footer abs">
  <p class="copyright abs">© Copyright 2021 Harrow Lane. All rights reserved.</p>
  <span class="social abs" style="left:618px" aria-label="Social profile"></span>
  <span class="social abs" style="left:647px" aria-label="Social profile"></span>
</footer>

</body>
</html>
```